International Shipping Company requires business card designs

We are a company based in Dubai UAE with our core business being shipping and container services. Our details can be found at www.coralwakefreight.com

We are not looking for a design that necessarily involves "ships or other shipping pictures", although some reference to the business in design or colour is encouraged.

Overall design of the card must be smart and depict the company which is very professional. Fonts, colours and layout must be very contemporary in look.

Shipping

```html
<!DOCTYPE html>
<html lang="en">
<head>
<meta charset="utf-8">
<title>Coral Wake International Shipping – Business Cards</title>
<link href="https://fonts.googleapis.com/css2?family=Open+Sans:wght@400;600;700&display=swap" rel="stylesheet">
<style>
  :root {
    --page-bg: #ececec;
    --card-white: #f7f7f8;
    --indigo: #3c3f8e;
    --ocean: #2b8ac6;
    --sky-light: #e9eef2;
    --sky-mid: #9fd2ea;
    --sky-deep: #6fbfe2;
    --text-light: #ffffff;
  }
  * { margin: 0; padding: 0; box-sizing: border-box; }
  html, body {
    width: 1200px; height: 900px; overflow: hidden;
    background: var(--page-bg);
    font-family: "Open Sans", Arial, sans-serif;
  }
  .canvas {
    position: relative; width: 1200px; height: 900px;
  }
  .card {
    position: absolute; top: 295px;
    width: 540px; height: 310px;
    overflow: hidden;
    box-shadow: 0 6px 18px rgba(0,0,0,0.12);
  }
  .card--front { left: 40px; background: var(--card-white); }
  .card--back {
    left: 620px;
    background: linear-gradient(200deg, var(--sky-light) 0%, var(--sky-mid) 55%, var(--sky-deep) 100%);
  }
  .card__waves { position: absolute; inset: 0; }

  .brand {
    position: absolute;
    display: flex; align-items: center; gap: 12px;
    color: var(--indigo);
    font-weight: 700;
  }
  .brand__dot {
    width: 46px; height: 46px; border-radius: 50%;
    background: var(--indigo); flex: none;
  }
  .brand__name {
    font-size: 30px; line-height: 1; letter-spacing: 1px;
    text-transform: uppercase;
  }
  .brand__sub {
    display: block; font-size: 11.5px; letter-spacing: 0.4px; margin-top: 4px;
  }
  .card--front .brand { left: 150px; top: 28px; }
  .card--back .brand { left: 138px; top: 88px; }

  .holder {
    position: absolute; left: 26px; top: 118px;
    color: var(--text-light);
  }
  .holder__name { font-size: 19px; font-weight: 400; }
  .holder__title { font-size: 10.5px; margin-top: 3px; }

  .contact {
    position: absolute; left: 330px; top: 200px;
    color: var(--text-light);
    font-size: 11px; line-height: 1.45; list-style: none;
  }

  .web-tab {
    position: absolute; right: 0; bottom: 26px;
    width: 300px; height: 40px;
    background: var(--ocean);
    border-radius: 20px 0 0 20px;
    color: var(--text-light);
    font-size: 14px;
    display: flex; align-items: center; padding-left: 36px;
  }
  .web-line {
    position: absolute; left: 0; right: 0; bottom: 0; height: 26px;
    background: linear-gradient(90deg, rgba(43,138,198,0) 0%, rgba(43,138,198,0.25) 100%);
  }
</style>
</head>
<body>
<main class="canvas">

  <section class="card card--front" aria-label="Business card front">
    <svg class="card__waves" viewBox="0 0 540 310" aria-hidden="true">
      <path d="M0 70 Q250 95 540 168 L540 178 Q250 108 0 86 Z" fill="var(--ocean)"/>
      <path d="M0 92 Q260 118 540 186 L540 310 L0 310 Z" fill="var(--indigo)"/>
    </svg>

    <div class="brand">
      <span class="brand__dot"></span>
      <div>
        <span class="brand__name">Coral Wake</span>
        <span class="brand__sub">INTERNATIONAL SHIPPING (L.L.C.)</span>
      </div>
    </div>

    <div class="holder">
      <p class="holder__name">Rami Khalid Osmani</p>
      <p class="holder__title">Manager Container &amp; HR Division</p>
    </div>

    <ul class="contact">
      <li>P.O. BOX 40562, Dubai, U.A.E.</li>
      <li>P: +971 4 3880210</li>
      <li>F: +971 4 3880211</li>
      <li>E: info@coralwakefreight.com</li>
    </ul>
  </section>

  <section class="card card--back" aria-label="Business card back">
    <div class="brand">
      <span class="brand__dot"></span>
      <div>
        <span class="brand__name">Coral Wake</span>
        <span class="brand__sub">INTERNATIONAL SHIPPING (L.L.C.)</span>
      </div>
    </div>
    <div class="web-line"></div>
    <div class="web-tab">www.coralwakefreight.com</div>
  </section>

</main>
</body>
</html>
```